BriarFen Anesthesia Partners, PC

I need a business card /logo for my new business. I would like it to have some type of ? EKG or medical symbol built into the name( I am on the North side of Lake Tessaly where mountains and water are visible.
I would like this saying on the front," Where Our Care Meets your Comfort"
My company provides anesthesia services to outparient endoscopy units, eye centers, pain & podiatry offices.

Target Market(s)

Gastroenterologists, podiatrists, eye doctors, pain doctors

Industry/Entity Type

Medical

Contact Information for Business Card

I would like to incorporate a medical symbol(EKG, stethoscope, etc) into the name or scenery if possible

Colors
3377b5
add136
fbee3d

Requirements
Must have
• Business name( BriarFen Anesthesia Partners,PCI).....
• "Where Our Care Meets your Comfort",
• my email: briarfenanesthesiapartners.example,
• 555-214-9087
Nice to have
• Incorporate water &/or mountains

```html
<!DOCTYPE html>
<html lang="en">
<head>
<meta charset="utf-8">
<title>BriarFen Anesthesia Partners, PCI – Business Card</title>
<link rel="stylesheet" href="https://fonts.googleapis.com/css2?family=Oswald:wght@400;500;700&family=Parisienne&display=swap">
<style>
  :root {
    --stage: #1c1c1e;
    --card: #ffffff;
    --brand-blue: #1f6fbf;
    --ink: #111111;
    --ink-soft: #3a3a3a;
    --sun: #f3a23a;
    --tagline: #4d86c4;
  }
  * { box-sizing: border-box; margin: 0; padding: 0; }
  html, body {
    width: 1200px; height: 871px; overflow: hidden;
    background: var(--stage);
  }
  .stage {
    position: relative; width: 1200px; height: 871px;
    display: flex; align-items: center; justify-content: center; gap: 40px;
  }
  .card {
    position: relative; width: 540px; height: 308px;
    background: var(--card); overflow: hidden;
    box-shadow: 0 12px 30px rgba(0,0,0,.5);
  }

  /* Brand name set as plain text */
  .brand {
    display: flex; align-items: center; gap: 10px;
    font-family: "Oswald", sans-serif; font-weight: 500;
    color: var(--brand-blue); text-transform: uppercase;
    letter-spacing: 1px; line-height: 1.15;
  }
  .brand-dot {
    flex: none; width: 22px; height: 22px; border-radius: 50%;
    background: var(--sun);
  }

  /* Back */
  .card-back {
    display: flex; flex-direction: column; align-items: center; justify-content: center;
    gap: 26px;
  }
  .card-back .brand { font-size: 26px; text-align: center; }
  .tagline {
    font-family: "Parisienne", cursive; font-size: 30px;
    color: var(--tagline);
  }

  /* Front */
  .card-front .brand {
    position: absolute; left: 26px; top: 112px; width: 220px;
    font-size: 18px;
  }
  .divider {
    position: absolute; left: 266px; top: 70px; width: 3px; height: 148px;
    background: var(--brand-blue);
  }
  .contact { position: absolute; left: 284px; top: 80px; right: 16px; }
  .person-name {
    font-family: "Oswald", sans-serif; font-weight: 700; font-size: 30px;
    color: var(--ink); line-height: 1;
  }
  .job-title {
    font-family: "Oswald", sans-serif; font-weight: 400; font-size: 12px;
    letter-spacing: 4px; color: var(--brand-blue); margin: 4px 0 12px;
  }
  .contact-line {
    display: flex; align-items: center; gap: 10px;
    font-family: "Oswald", sans-serif; font-weight: 500; font-size: 13px;
    letter-spacing: .4px; color: var(--ink-soft); margin-bottom: 8px;
    white-space: nowrap;
  }
  .contact-line svg { flex: none; fill: var(--brand-blue); }
  .band {
    position: absolute; left: 210px; right: 0; bottom: 0; height: 22px;
    background: var(--brand-blue);
  }
</style>
</head>
<body>
<main class="stage">
  <section class="card card-back" aria-label="Card back">
    <div class="brand"><span class="brand-dot"></span><span>BriarFen Anesthesia<br>Partners, PCI</span></div>
    <p class="tagline">Where Our Care Meets your Comfort</p>
  </section>

  <section class="card card-front" aria-label="Card front">
    <div class="brand"><span class="brand-dot"></span><span>BriarFen Anesthesia Partners, PCI</span></div>
    <div class="divider"></div>
    <div class="contact">
      <p class="person-name">Your Name</p>
      <p class="job-title">JOB TITLE</p>
      <p class="contact-line">
        <svg width="14" height="12" viewBox="0 0 14 12" aria-hidden="true"><path d="M1 3 Q7 -1 13 3 L11 5 L9 4 L9 3 Q7 2 5 3 L5 4 L3 5 Z M3 6 H11 L12 11 H2 Z"/></svg>
        555-214-9087
      </p>
      <p class="contact-line">
        <svg width="14" height="10" viewBox="0 0 14 10" aria-hidden="true"><path d="M0 0 H14 V10 H0 Z M1 1 L7 6 L13 1 Z" fill-rule="evenodd"/></svg>
        briarfenanesthesiapartners.example
      </p>
    </div>
    <div class="band"></div>
  </section>
</main>
</body>
</html>
```